Flyer needed for Seminar

Hello,
We are looking for eye-catching, inspiring marketing material for an educational seminar. We need 4 x 6 clubcards with the following info:

CLUBCARD FRONT:

Verander Academy Presents:

Stillness: Under The Surface
Unlock the hidden treasures of prayer
By. Shaykh Idris Kamal Al-Furati

Dates:Jan 23-25, 2015
Timings: Fri - 7pm - 9:30 pm; Sat/Sun - 9am - 8 pm

Location: Riverbend Grand Suites at Oakhaven Square
4385 Millbrook Lane, Plano, TX 75093

Seating is Limited. Register Today!
www.VeranderAcademy,com

CLUBCARD BACK:
In this unique seminar, learn how to connect spiritually with your Creator through prayer. Let us teach you the hidden meanings behind salah and why it is essential to your existence. Not only will the instructor impart the skills you'll need to master khushoo but he will delve more deeply, into the inner realms and intricacies of this ibadaa. As a result, the prayer will no longer be regarded as a mechanical chore, but an intimate meeting with the Divine. Through such insight, we hope you will leave this non-fiqh seminar with an awakened and unparalleled understanding of this fundamental pillar of Islam.

www.VeranderAcademy.com
For more info: Email - info@veranderacademy.com; Phone - 1-877-Verand4

Reason: I really appreciate all the submissions but am looking for something more eye-catching, something that really stirs ones interest and relates to the title of the seminar. Thank you!

```html
<!DOCTYPE html>
<html lang="en">
<head>
<meta charset="utf-8">
<title>Stillness: Under The Surface – Seminar Clubcard</title>
<link href="https://fonts.googleapis.com/css2?family=Lobster+Two:ital,wght@1,700&family=Open+Sans:wght@600;700&family=Roboto:wght@400&display=swap" rel="stylesheet">
<style>
  :root {
    --night-deep: #0a2450;
    --night-mid: #1a4d8c;
    --night-glow: #2a63a6;
    --divider: #0b1a33;
    --skyline: #04070d;
    --ink-white: #ffffff;
    --ink-navy: #0b1a38;
    --ornament: rgba(140, 180, 225, 0.35);
  }
  * { margin: 0; padding: 0; box-sizing: border-box; }
  html, body { width: 1200px; height: 848px; overflow: hidden; background: var(--divider); }
  .canvas { position: relative; width: 1200px; height: 848px; }

  .card {
    position: absolute; top: 0; height: 848px; overflow: hidden;
    background: radial-gradient(ellipse at 50% 40%, var(--night-glow) 0%, var(--night-mid) 40%, var(--night-deep) 100%);
    color: var(--ink-white); text-align: center;
  }
  .card--front { left: 0; width: 588px; }
  .card--back { left: 598px; width: 602px; }

  .skyline {
    position: absolute; left: 0; right: 0; bottom: 0;
    background: linear-gradient(to bottom, rgba(4,7,13,0) 0%, rgba(4,7,13,0.85) 35%, var(--skyline) 60%);
  }
  .card--front .skyline { height: 230px; }
  .card--back .skyline { height: 200px; }

  .ornament {
    position: absolute; left: 50%; transform: translateX(-50%);
    background: radial-gradient(ellipse, var(--ornament) 0%, rgba(140,180,225,0) 70%);
  }

  .line { position: absolute; left: 0; right: 0; z-index: 2; }
  .sans { font-family: "Roboto", sans-serif; font-weight: 400; }
  .bold { font-family: "Open Sans", sans-serif; font-weight: 700; }
  .script { font-family: "Lobster Two", cursive; font-style: italic; font-weight: 700; }

  .presenter { top: 32px; font-size: 19px; letter-spacing: 1.5px; }
  .title { top: 150px; font-size: 36px; line-height: 51px; padding: 0 40px; }
  .speaker { top: 382px; font-size: 31px; color: var(--ink-navy); }
  .dates { top: 437px; font-size: 44px; }
  .timings { top: 512px; font-size: 20px; line-height: 28px; letter-spacing: 0.5px; }
  .venue-label { top: 588px; height: 40px; display: flex; justify-content: center; align-items: center; gap: 14px; }
  .venue-label span { font-size: 28px; color: var(--ink-navy); }
  .venue-name { top: 642px; font-size: 20px; line-height: 28px; letter-spacing: 0.5px; }
  .venue-address { top: 703px; font-size: 18px; letter-spacing: 0.5px; }
  .front-cta { top: 782px; font-family: "Open Sans", sans-serif; font-weight: 600; font-size: 15px; line-height: 20px; letter-spacing: 0.8px; }

  .about {
    top: 228px; font-size: 17px; line-height: 27px; letter-spacing: 1px; text-transform: uppercase;
  }
  .back-cta { top: 655px; font-size: 21px; line-height: 28px; letter-spacing: 1px; }
  .contact { position: absolute; z-index: 2; left: 55px; display: flex; align-items: center; gap: 26px; font-size: 21px; letter-spacing: 1px; }
  .contact--email { top: 726px; }
  .contact--phone { top: 776px; }
  .contact svg { width: 46px; height: 34px; flex: none; }
</style>
</head>
<body>
<div class="canvas">

  <section class="card card--front">
    <div class="ornament" style="top:40px;width:360px;height:200px;" role="img" aria-label="Faint arabesque ornament behind the title"></div>

    <p class="line presenter sans">VERANDER ACADEMY PRESENTS</p>
    <h1 class="line title script">Stillness: Under The Surface<br>Unlock the hidden treasures<br>of prayer</h1>
    <p class="line speaker script">By. Shaykh Idris Kamal Al-Furati</p>
    <p class="line dates script">Jan 23-25, 2015</p>
    <p class="line timings sans">FRI - 7PM - 9:30 PM<br>SAT/SUN - 9AM - 8 PM</p>

    <div class="line venue-label">
      <svg width="120" height="12" viewBox="0 0 120 12" aria-hidden="true"><path d="M0 6 Q60 -2 120 6 Q60 10 0 6Z" fill="var(--ink-navy)"/></svg>
      <span class="script">Venue</span>
      <svg width="120" height="12" viewBox="0 0 120 12" aria-hidden="true"><path d="M0 6 Q60 -2 120 6 Q60 10 0 6Z" fill="var(--ink-navy)"/></svg>
    </div>
    <p class="line venue-name bold">Riverbend Grand Suites at<br>Oakhaven Square</p>
    <p class="line venue-address sans">4385 Millbrook Lane, Plano, TX 75093</p>

    <div class="skyline" role="img" aria-label="Silhouette of a mosque skyline with minarets and palm trees"></div>
    <p class="line front-cta">Seating is Limited. Register Today!<br>www.VeranderAcademy.com</p>
  </section>

  <section class="card card--back">
    <div class="ornament" style="top:45px;width:380px;height:110px;" role="img" aria-label="Arabesque ornament crest"></div>

    <p class="line about sans">
      In this unique seminar, learn how to connect<br>
      spiritually with your Creator throughprayer<br>
      let us teach you the hidden meanings behind<br>
      salah and why it is essential to your existence<br>
      not only will the instructor impart the skills<br>
      you'llneed to master khushoo but he willdelve<br>
      more deeply,into the inner realms and intricacies<br>
      of this ibadaa.as a result, the prayer will no<br>
      longer be regarded as a mechanical chore, but<br>
      an intimate meeting with the divine. Through<br>
      such insight, we hope you will leave this<br>
      non-fiqh seminar with an awakened and<br>
      unparalleled understanding of<br>
      this fundamental pillar of Islam.
    </p>

    <div class="skyline" role="img" aria-label="Silhouette of a mosque skyline with minarets and palm trees"></div>

    <p class="line back-cta bold">Seating is Limited. Register Today!<br>www.VeranderAcademy.com</p>
    <p class="contact contact--email bold">
      <svg viewBox="0 0 46 34" aria-hidden="true"><rect x="1" y="3" width="44" height="28" fill="#fff"/><path d="M1 3 L23 20 L45 3" fill="none" stroke="var(--skyline)" stroke-width="2.5"/></svg>
      info@veranderacademy.com
    </p>
    <p class="contact contact--phone bold">
      <svg viewBox="0 0 46 34" aria-hidden="true"><path d="M10 2 C5 4 3 9 6 15 C10 23 17 30 26 33 C31 34 35 31 36 27 L28 21 C26 22 24 24 22 23 C18 20 15 17 13 13 C12 11 14 9 16 8 Z" fill="#fff"/></svg>
      1-877-Verand4
    </p>
  </section>

</div>
</body>
</html>
```